Email Newsletter Banner

I require 2 new email newsletter and web banners to be made up.
I require the brand names to be included on the banner which are " Gadget Dispatch" and "Byte Wirez". I would also like some sort of imagery and also a "sign up here" button. Please see below examples:
https://fernvalepages.lumoshelf.com/
https://brightquarryhub.lumoshelf.com/
https://oakdalereads.lumoshelf.com/

```html
<!DOCTYPE html>
<html lang="en">
<head>
<meta charset="utf-8">
<title>Byte Wirez and Gadget Dispatch newsletters</title>
<link href="https://fonts.googleapis.com/css2?family=Montserrat:wght@300;400;600;700;800;900&display=swap" rel="stylesheet">
<style>
:root{
  --board:#6e6e70;
  --board-edge:#4a4a4c;
  --navy:#172b4f;
  --teal:#0e82b0;
  --paper:#ffffff;
  --ink:#34383f;
}
*{margin:0;padding:0;box-sizing:border-box}
html,body{width:688px;height:1200px;overflow:hidden}
body{
  background:radial-gradient(ellipse at 50% 45%,#8a8a8c 0%,var(--board) 55%,var(--board-edge) 100%);
  font-family:'Montserrat',sans-serif;position:relative;
}
.sheet{position:absolute;background:var(--paper);box-shadow:0 4px 14px rgba(0,0,0,.35)}
.banner{position:absolute;overflow:hidden}
.banner--byte{background:var(--navy)}
.banner--byte .stripe{position:absolute;left:0;top:0;width:9px;height:100%;background:var(--teal)}
.banner--byte .photo{position:absolute;right:0;top:0;width:160px;height:100%;
  background:linear-gradient(90deg,var(--navy) 0%,#3d587e 30%,#8a9bb0 60%,#5d7796 100%)}
.banner--gadget{background:linear-gradient(100deg,#f4f8fb 0%,#dde9f2 40%,#8fb0cc 70%,#1f3f6c 100%)}
.banner--gadget .photo{position:absolute;right:0;top:0;width:160px;height:100%;
  background:linear-gradient(100deg,rgba(255,255,255,0) 0%,rgba(110,150,190,.45) 45%,rgba(23,43,79,.75) 100%)}
.brand{position:absolute;font-weight:900;font-size:24px;line-height:23px;letter-spacing:.2px;white-space:nowrap}
.banner--byte .brand{color:#fff}
.brand .line1{color:var(--navy);display:block}
.brand .line2{color:var(--teal);display:block}
.btn{position:absolute;width:70px;height:22px;background:var(--teal);color:#fff;
  font-weight:800;font-size:7px;letter-spacing:.1px;display:flex;align-items:center;justify-content:center}
.heading{position:absolute;font-weight:900;font-size:23px;color:var(--navy);letter-spacing:.3px}
.copy{position:absolute;font-weight:400;font-size:6.4px;line-height:13.9px;color:var(--ink);text-align:justify}
.copy--right{line-height:13.3px}
.photo-block{position:absolute}
.footer{position:absolute;background:var(--navy);color:#fff}
.legal{position:absolute;left:0;width:100%;text-align:center;font-size:7.2px;font-weight:400}
.social{position:absolute;left:0;width:100%;display:flex;justify-content:center;gap:8px}
.social span{width:17px;height:17px;border-radius:50%;background:var(--teal)}
.bullets{position:absolute;list-style:none}
.bullets li{position:relative;padding-left:19px;font-weight:700;font-size:9.8px;color:var(--navy);height:15.6px;line-height:15.6px}
.bullets li::before{content:"";position:absolute;left:0;top:4.5px;width:7px;height:7px;border-radius:50%;background:var(--teal)}
</style>
</head>
<body>

<section class="sheet" style="left:37px;top:60px;width:298px;height:806px">
  <header class="banner banner--byte" style="left:0;top:0;width:298px;height:130px">
    <div class="stripe"></div>
    <div class="photo" role="img" aria-label="Photo of two businessmen talking at an office desk"></div>
    <div class="brand" style="left:23px;top:20px">BYTE WIREZ</div>
    <div class="btn" style="left:23px;top:55px">SIGN UP HERE</div>
  </header>
  <h2 class="heading" style="left:13px;top:146px">ABOUT</h2>
  <p class="copy" style="left:13px;top:180px;width:270px">Sed ut perspiciatis unde omnis iste natus erroptatem accloremque laudantium, totam rem aperiam, eaque ipsa qb illo inventore veritatis et quasi architecto beatae vitae dicta icamo enim ipsaoluptatem quia voluptas sit aspernatur aut odit aut fugit, sed consequuntur magni dolores eos qui ratione voluptatem sequi nesciunt. Neque porro quisquam est, qui dolorem ipsum quia dolor sit amet, consectetur, adipisci velit, sed quia non numquam eius modi tempora incidunt ut labore et dolore magnam aliquam volupaerat voluptatemSed ut perspiciatis unde omnis iste natus error sit voluptatem accusant doloremque laudantium, totam rem aperiam, eaque ipsa qnveritatis et quasi architecto beatae vitae dicta sunt explicamo enim ipsaolupuia voluptas sit aspernatur aut odit aut fugit, sed consequuntur magni dolores eos qui ratione voluptatem sequi nesciunt. Neque porro quisquam est, qui dolorem ipsum quia dolor sit amet, consectetur, adipisci velit, sed quia non numquam eius modi tempora incidunt ut labore et dolore magnam aliquam quaerat volupaerat volupttatem</p>
  <div class="photo-block" role="img" aria-label="Photo of colleagues reviewing charts at a bright desk with laptop and coffee" style="left:0;top:380px;width:298px;height:126px;background:linear-gradient(180deg,#ffffff 0%,#eef1f4 45%,#d9dee4 100%)"></div>
  <p class="copy" style="left:14px;top:524px;width:270px">Neque porro quisquam est, qui dolorem ipsum quia dolor sit amet, consectetur, adipisci velit, sed quia non numquam eius modi tempora incidunt ut labore et dolore magnam aliquam volupaerat voluptatemSed ut perspiciatis unde omnis iste natus error sit voluptatem accusant doloremque laudantium, totam rem aperiam, eaque ipsa qnveritatis et quasi architecto beatae vitae dicta sunt explicamo enim ipsaolupuia voluptas sit aspernatur aut odit aut fugit, sed consequuntur magni dolores eos qui ratione voluptatem sequi nesciunt. Neque porro quisquam est, qui dolorem ipsum quia dolor sit amet, consectetur, adipisci velit, sed quia non numquam eius modi tempora incidunt ut labore et dolore magnam aliquam quaerat volupaerat volupttatem</p>
  <div class="btn" style="left:14px;top:683px">SIGN UP HERE</div>
  <footer class="footer" style="left:0;top:731px;width:298px;height:75px">
    <p class="legal" style="top:15px">© 2022 Byte Wirez. All rights reserved.Privacy &nbsp;|&nbsp; Terms of Use</p>
    <div class="social" style="top:42px"><span></span><span></span><span></span></div>
  </footer>
</section>

<section class="sheet banner banner--byte" style="left:37px;top:873px;width:298px;height:129px">
  <div class="stripe"></div>
  <div class="photo" role="img" aria-label="Photo of two businessmen talking at an office desk"></div>
  <div class="brand" style="left:23px;top:20px">BYTE WIREZ</div>
  <div class="btn" style="left:23px;top:55px">SIGN UP HERE</div>
</section>

<section class="sheet banner banner--gadget" style="left:37px;top:1010px;width:298px;height:129px">
  <div class="photo" role="img" aria-label="Photo of hands typing on a laptop with digital data overlay"></div>
  <div class="brand" style="left:23px;top:20px"><span class="line1">GADGET</span><span class="line2">DISPATCH</span></div>
  <div class="btn" style="left:23px;top:80px">SIGN UP HERE</div>
</section>

<section class="sheet" style="left:353px;top:60px;width:298px;height:988px">
  <header class="banner banner--gadget" style="left:0;top:0;width:298px;height:130px">
    <div class="photo" role="img" aria-label="Photo of hands typing on a laptop with digital data overlay"></div>
    <div class="brand" style="left:23px;top:19px"><span class="line1">GADGET</span><span class="line2">DISPATCH</span></div>
    <div class="btn" style="left:23px;top:79px">SIGN UP HERE</div>
  </header>
  <p class="copy copy--right" style="left:23px;top:142px;width:252px">Lorem ipsum dolor sit amet, consectetur adipiscingd do eiusmod tempor incididunt ut labore et dolore magna aliqis ipsum suspendisse ultrices grcommodo viverra maecenas accumsan lacus vel facilisis. Lorem ipsum dolor sit amet, consectetur adipiscing elited do eiusmod tempor incididunt ut labore et dolore magna aliis ipsum suspendisse ultrices gravida. Risus commodo viverra maecenas accumsan lacus vel facilisis. Lorem ipsum dolor sit amet, consectetur adipiscing elit, sed do eiusmod tempor incididunt ut labore et dolore aliqm suspendisse ultric commodo viverra maecenas accumsan lacus vel facilisis.</p>
  <p class="copy copy--right" style="left:23px;top:275px;width:252px">Lorem ipsum dolor sit amet, consectetur adipiscingd do eiusmod tempor incididunt ut labore et dolore magna aliqupsum suspendisse ultrices grcommodo viverra maecenas accumsan lacus vel facilisis. Lorem ipsum dolor sit amet, consectetur adipiscinsed do eiusmod tempor incididunt ut labore et dolore magna aliis ipsum suspendisse ultrices gravida. Risus commodo viverra maecenas accumsan lacus vel facilisis. Lorem ipsum dolor sit amet, consectetur adipiscing elit, sed do eiusmod tempor incididunt ut</p>
  <ul class="bullets" style="left:23px;top:395px">
    <li>Ut enim ad minim veniam</li>
    <li>Quis nostrud exercitation ullamco</li>
    <li>Laboris nisi ut aliquip ex ea</li>
    <li>Commodo comonsequamot</li>
    <li>Duis aute irure dolreprehenderit</li>
  </ul>
  <p class="copy copy--right" style="left:23px;top:487px;width:252px">Lorem ipsum dolor sit amet, consectetur adipiscingd do eiusmod tempor incididunt ut labore et dolore magna aliqis ipsum suspendisse ultrices grcommodo viverra maecenas accumsan lacus vel facilisis. Lorem ipsum dolor sit amet, consectetur adipiscing elited do eiusmod tempor incididunt ut labore et dolore magna aliis ipsum suspendisse ultrices gravida. Risus commodo viverra maecenas accumsan lacus vel facilisis. Lorem ipsum dolor sit amet, consectetur adipiscing elit, sed do eiusmod tempor incididunt ut labore et dolore aliqm suspendisse ultric commodo viverra maecenas accumsan lacus vel facilisis.</p>
  <p class="copy copy--right" style="left:23px;top:620px;width:252px">Lorem ipsum dolor sit amet, consectetur adipiscingd do eiusmod tempor incididunt ut labore et dolore magna aliqupsum suspendisse ultrices grcommodo viverra maecenas accumsan lacus vel facilisis. Lorem ipsum dolor sit amet, consectetur adipiscinsed do eiusmod tempor incididunt ut labore et dolore magna aliis ipsum suspendisse ultrices gravida. Risus commodo viverra maecenas accumsan lacus vel facilisis. Lorem ipsum dolor sit amet, consectetur adipiscing elit, sed do eiusmod tempor incididunt ut</p>
  <div class="btn" style="left:23px;top:744px">SIGN UP HERE</div>
  <footer class="footer" style="left:0;top:891px;width:298px;height:97px">
    <p class="legal" style="top:41px">© 2022 Gadget Dispatch. All rights reserved.Privacy &nbsp;|&nbsp; Terms of Use</p>
    <div class="social" style="top:67px"><span></span><span></span><span></span></div>
  </footer>
  <div style="position:absolute;left:23px;top:788px;width:252px;height:130px;background:#f2f3f5"></div>
  <div class="photo-block" role="img" aria-label="Photo of two smiling coworkers looking at a tablet in an office" style="left:29px;top:792px;width:241px;height:120px;background:linear-gradient(90deg,#cfd3d6 0%,#8e9496 40%,#4b4f4a 65%,#a7a9a8 100%)"></div>
</section>

</body>
</html>
```